Consulting Firm of Business Savvy Super Geeks Needs Business Cards Redesigned

We need our business cards redesigned to reflect the company branding better, especially the website: www.TrelvoConsulting.com . Note the phrase "Business Savvy. Technology Smart" from the website. Also would love to see options that include verbiage of our offerings: Cloud Solutions, Digital Workspace, CRM Services, Dravelin Partner, Security Services, ERP Services.

Industry/Entity Type

Consulting

Contact Information for Business Card

Direct Phone #, Cell Phone #, Linkedin Address, Web address, Office Address

Font styles to use
Sans Serif

Requirements
Must have
• The cards should reflect the website.
• Clean design.
Nice to have
• Mentions to each of the business units / practices mentioned in the description.

```html
<!DOCTYPE html>
<html lang="en">
<head>
<meta charset="utf-8">
<title>Trelvo Consulting – Business Cards</title>
<link rel="stylesheet" href="https://fonts.googleapis.com/css2?family=Lato:wght@400;700;900&display=swap">
<style>
  :root {
    --navy: #253a4a;
    --blue: #1f6fc0;
    --orange: #ef8a3e;
    --white: #ffffff;
    --bg: #e9ecef;
  }
  * { margin: 0; padding: 0; box-sizing: border-box; }
  html, body { width: 1200px; height: 900px; overflow: hidden; }
  body {
    background: var(--bg);
    font-family: "Lato", sans-serif;
    position: relative;
  }
  .card {
    position: absolute;
    left: 280px;
    width: 640px;
    height: 366px;
    background: var(--white);
    overflow: hidden;
    box-shadow: 0 6px 18px rgba(30, 45, 60, 0.18);
  }
  .card--front { top: 62px; }
  .card--back { top: 472px; }
  .card__shapes { position: absolute; inset: 0; }

  /* Front */
  .brand {
    position: absolute;
    left: 40px;
    top: 150px;
    display: flex;
    align-items: center;
    gap: 12px;
  }
  .brand__mark { width: 22px; height: 22px; background: var(--blue); }
  .brand__name {
    font-weight: 900;
    font-size: 34px;
    line-height: 1;
    color: var(--navy);
    letter-spacing: -0.5px;
    white-space: nowrap;
  }
  .tagline {
    position: absolute;
    left: 318px;
    top: 14px;
    color: var(--white);
    font-weight: 900;
    font-size: 19px;
    line-height: 1.1;
    text-transform: uppercase;
    letter-spacing: 0.3px;
  }
  .services {
    position: absolute;
    left: 420px;
    top: 104px;
    list-style: none;
    color: var(--white);
    font-weight: 700;
    font-size: 18px;
    line-height: 1.45;
  }
  .services li::before { content: "+ "; font-weight: 900; }

  /* Back */
  .person {
    position: absolute;
    left: 30px;
    top: 152px;
    width: 280px;
    text-align: center;
  }
  .person__mark {
    width: 18px; height: 18px;
    background: var(--blue);
    margin: 0 auto 12px;
  }
  .person__name {
    font-weight: 900;
    font-size: 22px;
    color: var(--navy);
    text-transform: uppercase;
    letter-spacing: 0.5px;
    white-space: nowrap;
  }
  .person__title {
    font-weight: 700;
    font-size: 15px;
    color: var(--blue);
    letter-spacing: 1px;
  }
  .contact {
    position: absolute;
    left: 392px;
    top: 34px;
    color: var(--white);
    font-size: 13.5px;
    line-height: 1.45;
  }
  .contact__email { margin-bottom: 16px; font-size: 12.5px; }
  .contact__phones { margin-bottom: 16px; font-weight: 700; }
  .website {
    position: absolute;
    right: 24px;
    bottom: 24px;
    color: var(--white);
    font-weight: 900;
    font-size: 18px;
    white-space: nowrap;
  }
</style>
</head>
<body>

<section class="card card--front" aria-label="Card front">
  <svg class="card__shapes" viewBox="0 0 640 366" aria-hidden="true">
    <polygon points="255,0 640,0 640,74 305,74" fill="var(--orange)"/>
    <polygon points="305,74 640,74 640,366 420,366 390,140" fill="var(--blue)"/>
    <polyline points="262,84 360,132 396,366" fill="none" stroke="var(--blue)" stroke-width="3"/>
  </svg>
  <div class="brand">
    <span class="brand__mark"></span>
    <span class="brand__name">Trelvo Consulting</span>
  </div>
  <p class="tagline">Business Savvy.<br>Technology Smart.</p>
  <ul class="services">
    <li>Cloud Solutions</li>
    <li>Digital Workspace</li>
    <li>CRM Services</li>
    <li>Dravelin Partner</li>
    <li>Security Services</li>
    <li>ERP Services</li>
  </ul>
</section>

<section class="card card--back" aria-label="Card back">
  <svg class="card__shapes" viewBox="0 0 640 366" aria-hidden="true">
    <polygon points="320,0 640,0 640,292 367,292 360,150" fill="var(--blue)"/>
    <polygon points="367,292 640,292 640,366 372,366" fill="var(--orange)"/>
    <polyline points="290,0 332,150 345,366" fill="none" stroke="var(--blue)" stroke-width="3"/>
  </svg>
  <div class="person">
    <div class="person__mark"></div>
    <p class="person__name">Dana Whitcombe</p>
    <p class="person__title">CEO</p>
  </div>
  <div class="contact">
    <p class="contact__email">Dana.Whitcombe@trelvoconsulting.com</p>
    <p class="contact__phones">O: 555-206-0148<br>D: 555-838-0171<br>C: 555-580-0193</p>
    <p class="contact__address">218 Harlow St.<br>Brenton, PA 15990</p>
  </div>
  <p class="website">www.TrelvoConsulting.com</p>
</section>

</body>
</html>
```